Iconic Cool Labels for Amazing Coffee

I'm back again after a very successful logo design project, now looking for label designs!

NOTEs:

IF YOU SUBMIT A DESIGN YOU WILL DEFINITELY RECEIVE FEEDBACK. I think it's rude not to respond when somebody takes the time to devote their time and talent to a project like this.

THIS BRIEF IS LONG. Out of respect for you, the designers. I've put a lot of time into this to give you as much understanding as I can. I think if you are going to invest your time it is only right and proper that I do the same. So please don't be put off by the length - it is intended to save you time and energy.

THE BRIEF

We are launching a coffee website called Brewvantia aimed at those who really care about coffee and have a passion for getting the very best out of it. So far, we have a great logo (attached), we have the website under construction and with the look and feel decided.

We are not a mass market player - instead we are more like an online boutique. But, we are starting out and need to look chic in a way that doesn't involve large investments. So, our coffee will be packaged in bags (1kg and 250g) with brown paper exteriors (brown kraft) onto which we'll put self adhesive labels.This is where we need your help.

THE TASK
- Create the 2 "master" labels for the front of the bags
- Create the variety labels that go either on or somewhere around the master label
- Create a small label for the back of the bag that contains the required regulatory information

There are 2 "families" - each requiring a family label. They are our blends (there are 7 of these), our single origin coffees (there are 3 of these) and the fair trade organic.

MASTER LABELS - In my mind the main focus of this brief
For the front of the bag there will be a master label for each of the 2 families, with another self-adhesive label placed either on top of the master label or adjacent to it. The exception being the free trade organic - there is only one of these, so no over labelling required.

The master labels are the main game here. They need to be distinctive and tasteful. They should look "chic" but not "try hard". They should be different to each other yet clearly part of the same house.

Both master labels MUST include the Brewvantia logo (supplied) and must also include a small Tornaso logo somewhere. Tornaso is our roaster. Perhaps it might be "Proudly roasted by (Tornaso logo)", or something like that.

The master labels are needed in each of the 1kg and 250g sizes and should have the size displayed as a part of the label.

The 2 master labels are:
Blends - these are beans from multiple origins and are typically used for espresso, late etc. I'd prefer that the label doesn't say "blends".

Single Origin - these are coffees from a single place in the world. They are for enthusiasts who want to explore the nuance and subtlety of a single region. Rather than be made in an espresso machine (although they can be) siphons are where these truly come in to their own.

VARIETY LABEL
These will either be stuck in a designated space on the MASTER LABEL or will be stuck somewhere else on the usable area. There are 7 of these in the blends family and 3 in the single origins family. They may be all very similar in look and feel or they may be variations within a theme. What do you think they should be?

You may decide to make them look similar of different. You might have groups - e.g. the first four, the free trade organics and the decafs. (Though if you do please don't do the cliched thing and make the decafs blue!)

Our Varieties are:
BLENDS
The Waypost
The Devotee
The Sybarite
The Revelist
Free Trade Organic
Swiss Decafeinated
Mexican Mountain Decafeinated

SINGLE ORIGIN
Ethiopian Sotaru
Costa Rica La Tesca
Nicaraguan Verdalmira Superior

COMPLIANCE LABEL
This is a small label to go onto the back of the bag for all of our coffees. It contains all of the regulatory and compliance information. I'd like this to be small and reasonably unobtrusive, but clearly from the same "stable" as the other labels. This should be a regular shape so it's easy and quick to stick on, but not necessarily a rectangle - you pick.

It should contain:

Brewvantia
PO Box 4736
Prahran VIC 3181
www.brewvantia.com.au

Roasted, Blended & Packed in Australia
from Imported Beans

Store away from sunlight in a cool dry place

TECHNICAL DETAILS
The usable areas are (in portrait format)
1kg - 180mm high by 100mm wide
250g - 140mm high by 70mm wide

How much of this space you use and how you use it is up to you. My ingoing feeling is that using all of the available space would make it look "mass market" rather than premium. On the front, maybe there are a couple of small labels that are spaced, maybe there's one big label with an over sticker. I don't want to constrain you too much in this regard - except to say that unusual shapes like stars may be both slow and awkward to put onto the bags

THE CREATIVE SIDE
This is where you come in...
- Do you use all the space of just some of it (my guess is the latter)?
- One master on the front with an oversticker for variety or 2 separate labels?
- Rectangular labels or another shape (not jagged shapes please - too hard to stick evenly)
- Does the label contain, just words or does it have images, photos etc?
- Are the variety labels all similar or do they have a different look and feel?

ATTACHMENTS
- Brewvantia logo pack in zip file
- Tornaso logo
- Some photos I shared for the logo brief as examples
Updates

All, 

The files I thought I'd attached didn't get there the first time. I think I've corrected that now. Sorry for any hassle caused.

Cheers,
Gus

Target Market(s)

Our target customers have one thing in common - they are passionate about excellent coffee. While they come from all walks of life the image in my head is of young professionals that wear designer clothes - lots of black - and are passionate about design. They aspire to have Lurst furniture and care passionately about both design and functionality. They go to the cinema, but mainly arthouse and foreign. They visit the theatre and art galleries. They care about their coffee and the making of it might even be described as a ritual. They have separate grinders and espresso machines and are especially particular about everything to do with coffee - the beans (where they come from and how they are roasted), the grind, the making of the coffee itself, right down to the cups and glasses in which they are served.

Industry/Entity Type

Construction

Requirements
Must have
• A look and feel of premiumness without being staid. I think companies that have done this incredible well include Veltro, Sorna, Quell, Darui, KTR. They are clearly premium, but have a feeling of what I describe as understated cutting edge about them. There is a lot of work that has gone into all of their graphic material yet they don't look "try hard".The colour palate is quite narrow - black, white, silver/chrome, and various coffee shades ranging perhaps from the golden brown of the crema to the rich dark brown of a roasted bean.
Nice to have
• I would like the coffee bag to be something that people leave out because it looks cool an chic.
Should not have
• Please avoid the cliches. I was thrilled with the creativity in the logo work, so I am enthusiastic at the prospect of seeing the same here.

Importantly, please avoid steaming cups at all costs! Also, pictures of people sipping coffee and looking blissfully content are not what I'm looking for.

Also, out emphasis is italian style coffee - espresso, late etc rather than the long black coffee that comes out of a filter machine that is popular in the US - consequently images that connote that should be avoided.

```html
<!DOCTYPE html>
<html lang="en">
<head>
<meta charset="utf-8">
<title>Brewvantia Single Origin Labels</title>
<link rel="stylesheet" href="https://fonts.googleapis.com/css2?family=Cinzel:wght@500&family=Kaushan+Script&family=Arimo:ital,wght@0,400;1,400&display=swap">
<style>
  :root {
    --gold-deep: #a87a1c;
    --gold-mid: #d9ac45;
    --gold-light: #f6dd8c;
    --gold-pale: #fbeeb8;
    --roast: #3d230f;
    --band-white: #ffffff;
    --ink: #1e1408;
    --script-yellow: #f3e13a;
    --script-white: #ffffff;
    --canvas: #ffffff;
  }
  * { box-sizing: border-box; margin: 0; padding: 0; }
  html, body { width: 1200px; height: 701px; overflow: hidden; background: var(--canvas); }
  .label-row { position: relative; width: 1200px; height: 701px; }

  .label {
    position: absolute; top: 2px; width: 326px; height: 697px;
    background: linear-gradient(180deg, var(--gold-light) 0%, var(--gold-mid) 38%, var(--gold-pale) 62%, var(--gold-mid) 100%);
    border: 2px solid var(--gold-deep);
    overflow: hidden;
  }
  .label--nicaragua { left: 31px; }
  .label--ethiopia { left: 414px; }
  .label--costa-rica { left: 809px; }

  .label__pattern {
    position: absolute; left: 0; top: 0; width: 100%; height: 262px;
    background: radial-gradient(ellipse at 50% 40%, var(--gold-pale) 0%, var(--gold-mid) 55%, var(--gold-deep) 100%);
  }
  .brand-mark {
    position: absolute; left: 50%; top: 58px; width: 76px; height: 76px;
    transform: translateX(-50%); border-radius: 50%;
    background: var(--roast); border: 3px solid var(--gold-pale);
  }
  .brand-band {
    position: absolute; left: 14px; right: 14px; top: 157px; height: 32px;
    background: var(--band-white);
    display: flex; align-items: center; justify-content: center;
    font-family: "Cinzel", serif; font-weight: 500; font-size: 21px;
    letter-spacing: 6px; color: var(--roast);
  }
  .range-badge {
    position: absolute; left: 50%; top: 209px; width: 96px; height: 36px;
    transform: translateX(-50%); border-radius: 50%;
    background: var(--roast); border: 2px solid var(--gold-light);
    display: flex; align-items: center; justify-content: center;
    font-family: "Arimo", sans-serif; font-style: italic; font-size: 12px;
    color: var(--gold-light);
  }

  .origin-photo { position: absolute; left: 28px; top: 265px; width: 240px; height: 329px; }
  .bean-strip {
    position: absolute; left: 264px; top: 265px; width: 52px; height: 329px;
    background: linear-gradient(90deg, #4a2a12 0%, #7a4a22 40%, #3a200c 100%);
  }
  .label--nicaragua .origin-photo { background: linear-gradient(160deg, #5e6a3a 0%, #7c8a55 40%, #8a6a44 75%, #5a4630 100%); }
  .label--ethiopia .origin-photo { background: radial-gradient(ellipse at 45% 82%, #f7b43a 0%, #d9481c 25%, #8e1a10 60%, #4a0c08 100%); }
  .label--costa-rica .origin-photo { background: linear-gradient(180deg, #8a9ab2 0%, #6d7f98 30%, #7a8a5c 55%, #4f6a3a 100%); }

  .variety-name { position: absolute; font-family: "Kaushan Script", cursive; font-weight: 400; line-height: 1.05; }
  .variety-name--nicaragua {
    left: 46px; top: 444px; width: 200px; height: 138px;
    border: 2px solid var(--script-yellow);
    background: rgba(40, 30, 10, 0.25);
    color: var(--script-yellow); font-size: 27px; text-align: center; padding-top: 14px;
  }
  .variety-name--ethiopia {
    left: 36px; top: 290px; color: var(--script-white); font-size: 44px;
    text-shadow: 2px 2px 3px rgba(0,0,0,0.6);
  }
  .variety-name--ethiopia .line-two { display: block; padding-left: 96px; }
  .variety-name--costa-rica {
    left: 40px; top: 490px; color: var(--script-white); font-size: 32px;
    text-shadow: 1px 1px 2px rgba(0,0,0,0.5);
  }
  .variety-name--costa-rica .line-two { display: block; padding-left: 48px; }

  .roaster { position: absolute; left: 4px; top: 612px; width: 110px; text-align: center; }
  .roaster__credit {
    font-family: "Arimo", sans-serif; font-style: italic; font-size: 8px; color: var(--ink);
    display: block; margin-bottom: 3px;
  }
  .roaster__name {
    display: inline-flex; align-items: center; gap: 5px;
    font-family: "Arimo", sans-serif; font-size: 14px; color: var(--roast);
  }
  .roaster__dot { width: 10px; height: 10px; border-radius: 50%; background: var(--roast); }

  .net-weight {
    position: absolute; right: 6px; top: 660px;
    font-family: "Arimo", sans-serif; font-size: 14px; color: var(--ink);
  }
</style>
</head>
<body>
<main class="label-row">

  <article class="label label--nicaragua">
    <div class="label__pattern" role="img" aria-label="Gold mosaic tile pattern"></div>
    <div class="brand-mark"></div>
    <div class="brand-band">BREWVANTIA</div>
    <div class="range-badge">Single Origin</div>
    <div class="origin-photo" role="img" aria-label="Photograph of a turquoise-browed tropical bird perched on a post"></div>
    <div class="bean-strip" role="img" aria-label="Photograph of roasted coffee beans"></div>
    <h2 class="variety-name variety-name--nicaragua">Nicaraguan<br>Verdalmira<br>Superior</h2>
    <div class="roaster">
      <span class="roaster__credit">Proudly Roasted by</span>
      <span class="roaster__name"><span class="roaster__dot"></span>Tornaso</span>
    </div>
    <p class="net-weight">Net Wt. 1 Kg (35.27 oz)</p>
  </article>

  <article class="label label--ethiopia">
    <div class="label__pattern" role="img" aria-label="Gold mosaic tile pattern"></div>
    <div class="brand-mark"></div>
    <div class="brand-band">BREWVANTIA</div>
    <div class="range-badge">Single Origin</div>
    <div class="origin-photo" role="img" aria-label="Photograph of a lion silhouetted against a red sunset"></div>
    <div class="bean-strip" role="img" aria-label="Photograph of roasted coffee beans"></div>
    <h2 class="variety-name variety-name--ethiopia">Ethiopian<span class="line-two">Sotaru</span></h2>
    <div class="roaster">
      <span class="roaster__credit">Proudly Roasted by</span>
      <span class="roaster__name"><span class="roaster__dot"></span>Tornaso</span>
    </div>
    <p class="net-weight">Net Wt. 1 Kg (35.27 oz)</p>
  </article>

  <article class="label label--costa-rica">
    <div class="label__pattern" role="img" aria-label="Gold mosaic tile pattern"></div>
    <div class="brand-mark"></div>
    <div class="brand-band">BREWVANTIA</div>
    <div class="range-badge">Single Origin</div>
    <div class="origin-photo" role="img" aria-label="Painted view of a volcano above green hillside farmland"></div>
    <div class="bean-strip" role="img" aria-label="Photograph of roasted coffee beans"></div>
    <h2 class="variety-name variety-name--costa-rica">Costa Rica<span class="line-two">La Tesca</span></h2>
    <div class="roaster">
      <span class="roaster__credit">Proudly Roasted by</span>
      <span class="roaster__name"><span class="roaster__dot"></span>Tornaso</span>
    </div>
    <p class="net-weight">Net Wt. 1 Kg (35.27 oz)</p>
  </article>

</main>
</body>
</html>
```